Business Card and Word .doc header and footer required

I need a business card designed for my cybersecurity consulting company. Also required, is a header and footer to be ued for my word documents.
Attached is the Logo design, font and rgb used.

Industry/Entity Type

Cyber Security Consulting

Contact Information for Business Card

Name, Phone, email, website

Colors
0054AA
0677BA
7BADD7
CADEEF
E8F1F8

Requirements
Must have
• Sleek, modern

```html
<!DOCTYPE html>
<html lang="en">
<head>
<meta charset="utf-8">
<title>Harbor Ridge Consulting — Business Card and Letterhead</title>
<link rel="stylesheet" href="https://fonts.googleapis.com/css2?family=Montserrat:wght@500;600;700&display=swap">
<style>
  :root {
    --blue-deep: #0054AA;
    --blue: #0677BA;
    --blue-soft: #7BADD7;
    --blue-pale: #CADEEF;
    --blue-mist: #E8F1F8;
    --charcoal: #37373b;
    --ink: #2a2a2e;
    --paper: #f7f7f7;
    --backdrop: #e4e4e4;
    --watermark: #e6e6e6;
    --muted: #55585e;
  }
  * { box-sizing: border-box; margin: 0; padding: 0; }
  html, body { width: 1200px; height: 763px; overflow: hidden; }
  body {
    background: var(--backdrop);
    font-family: "Montserrat", Arial, sans-serif;
    position: relative;
  }

  /* Business card — front */
  .card { position: absolute; width: 460px; height: 263px; overflow: hidden; }
  .card-front {
    left: 90px; top: 70px;
    background: var(--charcoal);
    display: flex; flex-direction: column; align-items: center; justify-content: center; gap: 16px;
  }
  .brand-mark { width: 44px; height: 44px; border-radius: 50%; border: 3px solid var(--blue); }
  .brand-name {
    font-weight: 600; font-size: 22px; letter-spacing: 0.5px; color: #ffffff; text-align: center;
  }

  /* Business card — back */
  .card-back { left: 90px; top: 410px; background: var(--paper); }
  .card-back .person { position: absolute; left: 34px; top: 58px; }
  .person-name { font-weight: 700; font-size: 19px; color: var(--blue); letter-spacing: 0.3px; }
  .person-role { font-weight: 600; font-size: 12px; color: var(--blue-soft); margin-top: 4px; }
  .card-back .contacts { position: absolute; left: 34px; top: 160px; list-style: none; }
  .contacts li {
    display: flex; align-items: center; gap: 8px;
    font-size: 11px; font-weight: 500; color: var(--ink); line-height: 19px;
  }
  .contacts svg { width: 11px; height: 11px; flex: none; }
  .card-back .accent-bar { position: absolute; left: 34px; bottom: 0; width: 180px; height: 6px; background: var(--blue); }
  .card-back .deco-ring {
    position: absolute; right: -90px; top: -20px; width: 250px; height: 250px;
    border-radius: 50%; border: 14px solid var(--blue);
  }

  /* Letterhead */
  .letterhead {
    position: absolute; left: 640px; top: 42px; width: 480px; height: 679px;
    background: var(--paper); overflow: hidden;
  }
  .letterhead-header {
    position: absolute; left: 56px; top: 64px;
    display: flex; flex-direction: column; align-items: center; gap: 12px;
  }
  .letterhead-header .brand-mark { width: 40px; height: 40px; }
  .letterhead-header .brand-name { color: var(--ink); font-size: 17px; }
  .letterhead .watermark {
    position: absolute; left: 232px; top: 330px; width: 340px; height: 340px;
    border-radius: 50%; border: 14px solid var(--watermark);
  }
  .letterhead-footer {
    position: absolute; left: 58px; right: 38px; bottom: 26px;
    display: flex; justify-content: space-between;
    list-style: none;
  }
  .letterhead-footer li { display: flex; align-items: center; gap: 7px; font-size: 9px; font-weight: 500; color: var(--ink); }
  .letterhead-footer svg { width: 9px; height: 9px; }
  .footer-bar { position: absolute; left: 58px; bottom: 0; height: 5px; width: 390px; display: flex; }
  .footer-bar .bar-dark { flex: 3; background: var(--charcoal); }
  .footer-bar .bar-blue { flex: 1; background: var(--blue); }
</style>
</head>
<body>

  <section class="card card-front" aria-label="Business card front">
    <span class="brand-mark"></span>
    <p class="brand-name">HARBOR RIDGE CONSULTING</p>
  </section>

  <section class="card card-back" aria-label="Business card back">
    <div class="person">
      <p class="person-name">MARCO SILVA</p>
      <p class="person-role">Owner</p>
    </div>
    <ul class="contacts">
      <li><svg viewBox="0 0 12 12"><rect x="3" y="0.8" width="6" height="10.4" rx="1.2" fill="none" stroke="#0677BA" stroke-width="1.2"/></svg>555.014.2290</li>
      <li><svg viewBox="0 0 12 12"><rect x="0.8" y="2.5" width="10.4" height="7" fill="none" stroke="#0677BA" stroke-width="1.2"/><path d="M1 3l5 3.6L11 3" fill="none" stroke="#0677BA" stroke-width="1.2"/></svg>marco@harborridge.com</li>
      <li><svg viewBox="0 0 12 12"><circle cx="6" cy="6" r="5" fill="none" stroke="#0677BA" stroke-width="1.2"/><path d="M1 6h10M6 1c-2.5 3-2.5 7 0 10M6 1c2.5 3 2.5 7 0 10" fill="none" stroke="#0677BA" stroke-width="1"/></svg>www.harborridge.com</li>
    </ul>
    <span class="deco-ring"></span>
    <span class="accent-bar"></span>
  </section>

  <section class="letterhead" aria-label="Letterhead with header and footer">
    <header class="letterhead-header">
      <span class="brand-mark"></span>
      <p class="brand-name">HARBOR RIDGE CONSULTING</p>
    </header>
    <span class="watermark"></span>
    <ul class="letterhead-footer">
      <li><svg viewBox="0 0 12 12"><rect x="3" y="0.8" width="6" height="10.4" rx="1.2" fill="none" stroke="#0677BA" stroke-width="1.4"/></svg>555.014.2290</li>
      <li><svg viewBox="0 0 12 12"><rect x="0.8" y="2.5" width="10.4" height="7" fill="none" stroke="#0677BA" stroke-width="1.4"/><path d="M1 3l5 3.6L11 3" fill="none" stroke="#0677BA" stroke-width="1.4"/></svg>marco@harborridge.com</li>
      <li><svg viewBox="0 0 12 12"><circle cx="6" cy="6" r="5" fill="none" stroke="#0677BA" stroke-width="1.4"/><path d="M1 6h10M6 1c-2.5 3-2.5 7 0 10M6 1c2.5 3 2.5 7 0 10" fill="none" stroke="#0677BA" stroke-width="1.1"/></svg>www.harborridge.com</li>
    </ul>
    <div class="footer-bar"><span class="bar-dark"></span><span class="bar-blue"></span></div>
  </section>

</body>
</html>
```